Design Business Card for Velorant Kft

Size 91 x 61 mm

Velorant Kft

Company activities:
Digital Marketing Services, IT Services, Webhosting Services, Sales support services & SEO

Company is proud to be located in Hungary.

```html
<!DOCTYPE html>
<html lang="en">
<head>
<meta charset="utf-8">
<title>Velorant Kft – Business Cards</title>
<link href="https://fonts.googleapis.com/css2?family=Open+Sans:wght@400;700&display=swap" rel="stylesheet">
<style>
  :root{
    --bg:#8a8a8a;
    --paper:#ffffff;
    --blue:#29a6df;
    --orange:#f6921e;
    --ink:#111111;
  }
  *{margin:0;padding:0;box-sizing:border-box}
  html,body{width:1200px;height:900px;overflow:hidden}
  body{background:var(--bg);font-family:"Open Sans",Arial,sans-serif;position:relative}
  .card{
    position:absolute;left:327px;width:546px;height:366px;
    background:var(--paper);border-radius:26px;overflow:hidden;
  }
  .card--blue{top:70px}
  .card--orange{top:466px}
  .card__band{position:absolute;left:0;right:0;top:150px;bottom:0}
  .card--blue .card__band{background:var(--blue)}
  .card--orange .card__band{background:var(--orange)}
  .brand{position:absolute;left:0;right:0;top:48px;text-align:center;
    font-size:44px;font-weight:700;color:var(--ink);line-height:1}
  .holder{position:absolute;left:34px;top:176px;color:var(--ink)}
  .holder__name{font-size:14px;font-weight:700;text-transform:uppercase}
  .holder__role{font-size:10px;margin-top:1px}
  .holder__reg{font-size:9px;margin-top:14px;line-height:1.5}
  .divider{position:absolute;left:296px;top:166px;width:2px;height:176px;background:var(--ink)}
  .contact{position:absolute;left:312px;top:166px;color:var(--ink);font-size:15px;line-height:1.25}
  .contact__address{margin-bottom:8px}
  .contact__row{display:flex;align-items:center;gap:8px;height:27px}
  .contact__row svg{width:20px;height:20px;flex:none}
</style>
</head>
<body>

<section class="card card--blue" aria-label="Business card, blue version">
  <div class="card__band"></div>
  <p class="brand">Velorant Kft</p>
  <div class="holder">
    <p class="holder__name">Bence Halmi</p>
    <p class="holder__role">Manager Director</p>
    <p class="holder__reg">Company registration: 02-09-071368<br>VAT: HU20461938</p>
  </div>
  <div class="divider"></div>
  <div class="contact">
    <p class="contact__address">Fenyves utca 12,<br>7621 Pécs, Hungary</p>
    <p class="contact__row">
      <svg viewBox="0 0 20 20"><circle cx="10" cy="10" r="10" fill="#111"/><path d="M7 5l2 2-1 1.5c.8 1.6 1.9 2.7 3.5 3.5L13 11l2 2-1.5 1.5C10 14 6 10 5.5 6.5z" fill="#fff"/></svg>
      +3672 555 014</p>
    <p class="contact__row">
      <svg viewBox="0 0 20 20"><circle cx="10" cy="10" r="10" fill="#111"/><rect x="6" y="5" width="8" height="4" fill="#fff"/><rect x="4.5" y="9" width="11" height="5" rx="1" fill="#fff"/><rect x="7" y="12" width="6" height="3" fill="#111"/></svg>
      +3672 555 015</p>
    <p class="contact__row">
      <svg viewBox="0 0 20 20"><circle cx="10" cy="10" r="10" fill="#111"/><rect x="5" y="6.5" width="10" height="7" fill="#fff"/><path d="M5 6.5l5 4 5-4" stroke="#111" fill="none"/></svg>
      admin@velorant.com</p>
    <p class="contact__row">
      <svg viewBox="0 0 20 20"><circle cx="10" cy="10" r="10" fill="#111"/><circle cx="10" cy="10" r="5" stroke="#fff" fill="none"/><path d="M5 10h10M10 5c-2.5 3-2.5 7 0 10M10 5c2.5 3 2.5 7 0 10" stroke="#fff" fill="none"/></svg>
      www.velorant.com</p>
  </div>
</section>

<section class="card card--orange" aria-label="Business card, orange version">
  <div class="card__band"></div>
  <p class="brand">Velorant Kft</p>
  <div class="holder">
    <p class="holder__name">Bence Halmi</p>
    <p class="holder__role">Manager Director</p>
    <p class="holder__reg">Cégjegyzékszám: 02-09-071368<br>Közösségi adószám: HU20461938</p>
  </div>
  <div class="divider"></div>
  <div class="contact">
    <p class="contact__address">7621 Pécs,<br>Fenyves utca 12.</p>
    <p class="contact__row">
      <svg viewBox="0 0 20 20"><circle cx="10" cy="10" r="10" fill="#111"/><path d="M7 5l2 2-1 1.5c.8 1.6 1.9 2.7 3.5 3.5L13 11l2 2-1.5 1.5C10 14 6 10 5.5 6.5z" fill="#fff"/></svg>
      72/555 014</p>
    <p class="contact__row">
      <svg viewBox="0 0 20 20"><circle cx="10" cy="10" r="10" fill="#111"/><rect x="6" y="5" width="8" height="4" fill="#fff"/><rect x="4.5" y="9" width="11" height="5" rx="1" fill="#fff"/><rect x="7" y="12" width="6" height="3" fill="#111"/></svg>
      72/555 015</p>
    <p class="contact__row">
      <svg viewBox="0 0 20 20"><circle cx="10" cy="10" r="10" fill="#111"/><rect x="5" y="6.5" width="10" height="7" fill="#fff"/><path d="M5 6.5l5 4 5-4" stroke="#111" fill="none"/></svg>
      admin@velorant.hu</p>
    <p class="contact__row">
      <svg viewBox="0 0 20 20"><circle cx="10" cy="10" r="10" fill="#111"/><circle cx="10" cy="10" r="5" stroke="#fff" fill="none"/><path d="M5 10h10M10 5c-2.5 3-2.5 7 0 10M10 5c2.5 3 2.5 7 0 10" stroke="#fff" fill="none"/></svg>
      www.velorant.hu</p>
  </div>
</section>

</body>
</html>
```